Haldor Snekker AS
Buiness cards for haldor snekker as
Haldor Snekker AS - Construction
Creative Brief
Simple
Tobias Kranveldt
CEO
Lerkeskogveien 14 0587 OSLO Norway
post@haldorsnekker.example
www.haldorsnekker.example
Org. nr.: 836 402 517
Its for a company that expanse fast within big building sites
come up with something!?! we make your investment possible

```html
<!DOCTYPE html>
<html lang="no">
<head>
<meta charset="utf-8">
<title>Haldor Snekker AS – visittkort</title>
<link rel="stylesheet" href="https://fonts.googleapis.com/css2?family=Open+Sans:wght@400;600;700&display=swap">
<style>
  :root {
    --stage: #2f2f2f;
    --brand-red: #d4201a;
    --card-white: #f7f7f7;
    --ink: #3a3a3a;
    --ink-soft: #6d6d6d;
    --paper: #ffffff;
  }
  * { margin: 0; padding: 0; box-sizing: border-box; }
  html, body { width: 1200px; height: 751px; overflow: hidden; }
  body {
    background: var(--stage);
    font-family: "Open Sans", Arial, sans-serif;
    position: relative;
  }
  .card {
    position: absolute;
    top: 216px;
    width: 492px;
    height: 283px;
    overflow: hidden;
  }
  .card--front { left: 91px; background: var(--brand-red); }
  .card--back { left: 619px; background: var(--card-white); }

  .symbol-area {
    position: absolute;
    left: 0; top: 96px;
    width: 262px; height: 187px;
    background: var(--paper);
  }

  .contact {
    position: absolute;
    left: 17px; top: 124px;
    width: 236px;
    color: var(--ink);
    font-size: 11px;
    line-height: 14px;
    white-space: nowrap;
  }
  .contact__address { margin-bottom: 8px; }
  .contact__list { list-style: none; }
  .contact__item {
    display: flex; align-items: center;
    height: 19.5px;
  }
  .contact__item svg { width: 11px; height: 11px; margin-right: 9px; fill: var(--brand-red); flex: none; }
  .contact__org { margin-top: 6px; }

  .person {
    position: absolute;
    right: 24px; top: 222px;
    text-align: right;
    color: var(--paper);
  }
  .person__name { font-size: 17px; font-weight: 700; line-height: 20px; }
  .person__role { font-size: 11.5px; line-height: 16px; }

  .brand {
    position: absolute;
    left: 0; right: 0; top: 124px;
    display: flex; justify-content: center; align-items: center;
  }
  .brand__mark {
    width: 40px; height: 40px;
    background: var(--brand-red);
    margin-right: 12px;
  }
  .brand__name {
    font-size: 24px; font-weight: 600;
    color: var(--ink);
    letter-spacing: 1px;
  }
  .web {
    position: absolute;
    left: 0; right: 0; top: 240px;
    text-align: center;
    color: var(--ink-soft);
    font-size: 11px;
    letter-spacing: 2px;
  }
</style>
</head>
<body>
  <section class="card card--front">
    <div class="symbol-area" role="img" aria-label="Area for the brand's large white animal-head symbol"></div>
    <div class="contact">
      <p class="contact__address">Lerkeskogveien 14<br>0587 OSLO, Norway</p>
      <ul class="contact__list">
        <li class="contact__item"><svg viewBox="0 0 12 12"><rect x="3" y="0" width="6" height="12" rx="1"/></svg>+47 9000 1234</li>
        <li class="contact__item"><svg viewBox="0 0 12 12"><path d="M1 4h10v7H1z M3 1h6v3H3z"/></svg>+47 2100 5678</li>
        <li class="contact__item"><svg viewBox="0 0 12 12"><path d="M0 2h12v8H0z"/></svg>post@haldorsnekker.example</li>
        <li class="contact__item"><svg viewBox="0 0 12 12"><circle cx="6" cy="6" r="6"/></svg>www.haldorsnekker.example</li>
      </ul>
      <p class="contact__org">Org. nr.: 836 402 517</p>
    </div>
    <div class="person">
      <p class="person__name">Tobias Kranveldt</p>
      <p class="person__role">CEO</p>
    </div>
  </section>

  <section class="card card--back">
    <div class="brand">
      <span class="brand__mark"></span>
      <span class="brand__name">HALDOR SNEKKER AS</span>
    </div>
    <p class="web">www.haldorsnekker.example</p>
  </section>
</body>
</html>
```